SkyvoraQ Business Cards and Stationary Design

Need a design for our business cards and stationary. I want to carry on the theme of the logo. I want the business cards to have a design on the back. I would like the business cards and the stationary to carry the same theme, design scheme, and branding

Target Market(s)

Airlines and Maintenance Facilities

Industry/Entity Type

Aviation

Contact Information for Business Card

Name
Position Title
Address: 4827 Tollbeck Lane, Fort Pierce, Florida, 34951
Office Number
Mobile Number
Email
Website

Font styles to use
Serif
Sans Serif

Colors

Designer to choose colors to be used in the design.

```html
<!DOCTYPE html>
<html lang="en">
<head>
<meta charset="UTF-8">
<title>SkyvoraQ Business Card</title>
<link href="https://fonts.googleapis.com/css2?family=Exo+2:wght@400;600;700&display=swap" rel="stylesheet">
<style>
  :root {
    --backdrop: #8a8a8a;
    --card-light: #ededed;
    --navy: #0b2a57;
    --navy-deep: #0a2650;
    --ink: #2b2b2b;
    --rule: #a9a9a9;
    --white: #ffffff;
    --accent: #1e8ee0;
  }
  * { margin: 0; padding: 0; box-sizing: border-box; }
  html, body { width: 1200px; height: 1200px; overflow: hidden; }
  body {
    background: var(--backdrop);
    font-family: "Exo 2", sans-serif;
    position: relative;
  }
  .card {
    position: absolute;
    top: 310px;
    width: 364px;
    height: 594px;
    box-shadow: 2px 3px 6px rgba(0,0,0,0.35);
    text-align: center;
  }
  .card-front { left: 234px; background: var(--card-light); color: var(--ink); }
  .card-back { left: 627px; width: 370px; background: var(--navy-deep); color: var(--white); }

  .brand-circle {
    position: absolute;
    left: 50%;
    border-radius: 50%;
    transform: translateX(-50%);
  }
  .card-front .brand-circle {
    top: 105px; width: 90px; height: 90px;
    border: 7px solid var(--accent);
  }
  .card-back .brand-circle {
    top: 222px; width: 102px; height: 102px;
    border: 7px solid var(--white);
  }
  .wordmark {
    position: absolute;
    left: 0; right: 0;
    font-weight: 700;
    letter-spacing: 4px;
    line-height: 1;
  }
  .card-front .wordmark { top: 214px; font-size: 33px; color: var(--navy); }
  .card-back .wordmark { top: 340px; font-size: 37px; color: var(--white); }

  .person-name {
    position: absolute; left: 0; right: 0; top: 328px;
    font-size: 24px; font-weight: 700; color: var(--navy); letter-spacing: 0.5px;
  }
  .person-title {
    position: absolute; left: 0; right: 0; top: 355px;
    font-size: 17px;
  }
  .rule {
    position: absolute; left: 78px; width: 208px; height: 1px;
    background: var(--rule);
  }
  .rule-top { top: 387px; }
  .rule-bottom { top: 497px; }
  .contact-list {
    position: absolute; left: 0; right: 0; top: 399px;
    list-style: none; font-size: 16px; line-height: 21.7px;
  }
  .contact-list b { color: var(--navy); font-weight: 700; }
  .contact-list .web { color: var(--navy); font-weight: 700; }
  .address {
    position: absolute; left: 0; right: 0; top: 510px;
    font-size: 16px; line-height: 21px; font-style: normal;
  }
  .back-web {
    position: absolute; left: 0; right: 0; top: 525px;
    font-size: 18px; letter-spacing: 1.2px;
  }
</style>
</head>
<body>
  <section class="card card-front">
    <div class="brand-circle"></div>
    <div class="wordmark">SKYVORAQ</div>
    <div class="person-name">MARCUS DELANE</div>
    <div class="person-title">Managing Director</div>
    <div class="rule rule-top"></div>
    <ul class="contact-list">
      <li><b>P:</b> 044-310 582 647</li>
      <li><b>M:</b> 044-310 582 647</li>
      <li><b>E:</b> hello@skyvoraq.com</li>
      <li class="web">www.skyvoraq.com</li>
    </ul>
    <div class="rule rule-bottom"></div>
    <address class="address">4827 Tollbeck Lane<br>Fort Pierce, Florida, 34951</address>
  </section>

  <section class="card card-back">
    <div class="brand-circle"></div>
    <div class="wordmark">SKYVORAQ</div>
    <div class="back-web">WWW.SKYVORAQ.COM</div>
  </section>
</body>
</html>
```